Bi-fold brochure/business card for Restoration company
Marketing brochure and Business card
Bi-fold brochure/business card for Restoration company - Construction
Creative Brief
Construction
Insurance adjusters, property management cos, home owners, plumbers, roofers, builders etc.
(Need a bi-fold brochure, simple, elegant and classic) (logo is draft #135) Page#1: When unexpected happens…., expect…. Logo & Company Name Complete Restoration & Reconstruction services Water Damage  Sewer Backup  Mold  Fire & Smoke Residential  Commercial  Institutional (kind of footnotes with small font compared to rest of the font in this page) (Have the logo of BTFQN and KDW in the corner somewhere in the first page) Page #2: Key Features: • BTFQN Certified Firm • Professionally Managed Company (KDW® certified) • Excellence, Ethical and Reliable • Prompt and Competitive Estimates • Committed to Response within 60 minutes • Highest Priority for Health & Safety • Green & Eco-friendly • Exceptional Customer care • Cutting Edge, Tested & Approved Restoration Process • High Quality and Latest Equipments • 24x7 Dedicated & Prompt service (Some pictures of water/mold/fire/smoke/sewage in Page 2 & 3. If you can find any suitable pictures can use it and I am also working on the pictures) Page #3: Capabilities: • Water Damage Remediation • Sewer Backup Remediation • Mold Inspection & Remediation • Fire/Smoke Damage Remediation • Structural Drying • Security Board-up • Content Pack-out & Cleaning • Odor Removal & Control • Carpet Cleaning • Complete Reconstruction o Drywall and Insulation o Roofing o Flooring o Painting Page #4: Company name with Logo, www.qualmend.ca & ph no: 403-771-4286 (half the page) (rest half of the page have the below 4 items in some box type with pictures and text embossed on top of pict) Water (inside a box and the text on top of a picture representing water) Mold (inside a box and the text on top of a picture representing mold, something like http://www.brelvinhome.com/is-this-mold) Fire/Smoke (inside a box and the text on top of a picture representing Fire or/and smoke) Reconstruction (inside a box and the text on top of a picture representing reconstruction)

```html
<!DOCTYPE html>
<html lang="en">
<head>
<meta charset="utf-8">
<title>qualmend – Brochure &amp; Business Card</title>
<link rel="stylesheet" href="https://fonts.googleapis.com/css2?family=Open+Sans:wght@400;600;700;800&display=swap">
<style>
  :root{
    --blue:#1b5fb0;
    --blue-deep:#0e3f80;
    --green:#7cc242;
    --green-deep:#4e9a2a;
    --charcoal:#2a2c2e;
    --black:#141516;
    --white:#ffffff;
    --grey:#b9bec4;
    --stage:#ecebe7;
  }
  *{box-sizing:border-box;margin:0;padding:0}
  html,body{width:1200px;height:899px;overflow:hidden}
  body{background:var(--stage);font-family:"Open Sans",Arial,sans-serif;position:relative;color:var(--white)}

  .spread{position:absolute;width:540px;height:340px;display:flex;box-shadow:0 3px 10px rgba(0,0,0,.25)}
  .spread--outer-a{left:30px;top:30px}
  .spread--outer-b{left:630px;top:30px}
  .spread--inner{left:30px;top:420px}

  .panel{position:relative;width:270px;height:340px;overflow:hidden;background:var(--charcoal)}
  .panel>svg.swirl{position:absolute;inset:0;width:100%;height:100%}

  .photo{position:absolute;background:linear-gradient(135deg,#6f8797,#3a4a55)}
  .photo--water{background:linear-gradient(160deg,#9fb9c9,#4d6e86)}
  .photo--mold{background:linear-gradient(160deg,#e3e3e0,#9a9d98)}
  .photo--fire{background:linear-gradient(160deg,#5b4a3c,#231d18)}
  .photo--rebuild{background:linear-gradient(160deg,#a68b68,#5d4a35)}
  .photo--sand{background:linear-gradient(160deg,#e6d3b3,#c7a77c)}
  .photo--house-water{background:linear-gradient(160deg,#dfe8ec,#7c9cb0)}
  .photo--tech{background:linear-gradient(160deg,#f2f2f2,#b9bcbe)}
  .photo--equipment{background:linear-gradient(160deg,#5d7aa0,#2b3a52)}

  .tile-label{position:absolute;font-size:10px;font-weight:700;color:var(--white);text-shadow:0 1px 2px rgba(0,0,0,.7)}

  .logo{position:absolute;display:flex;align-items:center;gap:5px}
  .logo__mark{width:14px;height:14px;border-radius:50%;background:var(--green)}
  .logo__name{font-weight:700;font-size:20px;color:var(--white);letter-spacing:.2px}
  .logo__tag{position:absolute;font-size:5.5px;color:var(--grey)}

  .headline{position:absolute;font-weight:800;font-size:17px;line-height:1.2;color:var(--white)}
  .contact{position:absolute;font-size:7px;color:var(--white);line-height:1.4}
  .service-line{position:absolute;font-size:6.5px;color:var(--white)}

  .sector-box{position:absolute;background:var(--blue);padding:5px 7px;font-size:6.5px;line-height:1.55;font-weight:600}
  .sector-box li{list-style:none}
  .sector-box li::before{content:"■ ";color:var(--green);font-size:5px}
  .sector-list{position:absolute;font-size:6.5px;line-height:1.55;font-weight:600}
  .sector-list li{list-style:none}
  .sector-list li::before{content:"■ ";color:var(--blue);font-size:5px}

  .section-title{position:absolute;font-weight:800;font-size:17px;color:var(--white)}
  .title-dot{position:absolute;width:16px;height:16px;border-radius:50%;background:var(--green)}
  .bullets{position:absolute;font-size:6.6px;line-height:1.62}
  .bullets li{list-style:none;padding-left:8px;position:relative}
  .bullets li::before{content:"";position:absolute;left:0;top:3px;width:4px;height:4px;background:var(--green);border-radius:50%}
  .bullets .sub{padding-left:16px}
  .bullets .sub::before{left:9px;background:var(--white)}

  .card{position:absolute;width:250px;height:145px;box-shadow:0 3px 8px rgba(0,0,0,.25);overflow:hidden}
  .card--front{left:640px;top:470px;background:var(--white);color:var(--charcoal)}
  .card--front-b{left:910px;top:470px;background:var(--white);color:var(--charcoal)}
  .card--back{left:775px;top:635px;background:var(--charcoal)}
  .card>svg{position:absolute;inset:0;width:100%;height:100%}
  .card .logo__name{color:var(--charcoal);font-size:18px}
  .card--back .logo__name{color:var(--white)}
  .card__person{position:absolute;right:12px;top:38px;width:105px;font-size:6px;line-height:1.5;color:var(--charcoal)}
  .card__person strong{display:block;font-size:8px}
  .card__foot{position:absolute;font-size:5.5px;color:var(--white)}
</style>
</head>
<body>

<!-- Outer spread, version A -->
<section class="spread spread--outer-a">
  <div class="panel panel--back">
    <svg class="swirl" viewBox="0 0 270 340" preserveAspectRatio="none" aria-hidden="true">
      <rect width="270" height="340" fill="#2a2c2e"/>
      <path d="M0 0 H150 C120 80 110 200 150 340 H0 Z" fill="#1b5fb0"/>
      <path d="M0 0 H128 C100 90 95 210 130 340 H0 Z" fill="#0e3f80"/>
      <path d="M150 340 C170 260 230 220 270 215 V340 Z" fill="#7cc242"/>
      <path d="M175 340 C190 280 235 250 270 245 V340 Z" fill="#2a2c2e"/>
    </svg>
    <div class="photo photo--water" style="left:8px;top:8px;width:110px;height:72px" role="img" aria-label="Water damage in a flooded room"></div>
    <span class="tile-label" style="left:14px;top:62px">Water</span>
    <div class="photo photo--mold" style="left:8px;top:86px;width:110px;height:72px" role="img" aria-label="Technician in protective suit treating mold"></div>
    <span class="tile-label" style="left:14px;top:140px">Mold</span>
    <div class="photo photo--fire" style="left:8px;top:164px;width:110px;height:80px" role="img" aria-label="Fire and smoke damaged interior"></div>
    <span class="tile-label" style="left:14px;top:226px">Fire/Smoke</span>
    <div class="photo photo--rebuild" style="left:8px;top:250px;width:110px;height:82px" role="img" aria-label="Room under reconstruction with exposed framing"></div>
    <span class="tile-label" style="left:14px;top:314px">Reconstruction</span>
    <ul class="sector-box" style="left:176px;top:10px">
      <li>Residential</li><li>Commercial</li><li>Institutional</li>
    </ul>
    <div class="logo" style="left:150px;top:282px"><span class="logo__mark"></span><span class="logo__name">qualmend</span></div>
    <p class="contact" style="left:168px;top:308px">www.qualmend.ca<br>Call: 403-771-4286</p>
  </div>
  <div class="panel panel--front">
    <svg class="swirl" viewBox="0 0 270 340" preserveAspectRatio="none" aria-hidden="true">
      <rect width="270" height="340" fill="#1a1b1c"/>
      <path d="M0 150 C60 170 180 160 270 110 V340 H0 Z" fill="#7cc242"/>
      <path d="M0 162 C70 185 180 178 270 130 V340 H0 Z" fill="#2a2c2e"/>
      <path d="M0 300 C80 280 180 290 270 320 V340 H0 Z" fill="#1b5fb0"/>
    </svg>
    <div class="photo photo--sand" style="left:0;top:0;width:270px;height:150px;clip-path:path('M0 0 H270 V110 C180 160 60 170 0 150 Z')" role="img" aria-label="Drawing of a house traced in sand"></div>
    <h1 class="headline" style="left:100px;top:180px">When<br>unexpected<br>happens….<br>expect…</h1>
    <div class="logo" style="left:108px;top:268px"><span class="logo__mark"></span><span class="logo__name">qualmend</span></div>
    <p class="logo__tag" style="left:128px;top:292px">Complete Restoration &amp; Reconstruction services</p>
    <p class="service-line" style="left:92px;top:322px">Water Damage • Sewer Backup • Mold • Fire &amp; Smoke</p>
  </div>
</section>

<!-- Outer spread, version B -->
<section class="spread spread--outer-b">
  <div class="panel panel--back">
    <svg class="swirl" viewBox="0 0 270 340" preserveAspectRatio="none" aria-hidden="true">
      <rect width="270" height="340" fill="#2a2c2e"/>
      <path d="M0 230 C80 220 190 250 270 300 V340 H0 Z" fill="#7cc242"/>
      <path d="M0 250 C80 245 190 270 270 320 V340 H0 Z" fill="#1a1b1c"/>
    </svg>
    <div class="photo photo--water" style="left:6px;top:18px;width:126px;height:100px" role="img" aria-label="Water damaged basement"></div>
    <div class="photo photo--mold" style="left:138px;top:18px;width:126px;height:100px" role="img" aria-label="Mold remediation in protective suit"></div>
    <div class="photo photo--fire" style="left:6px;top:124px;width:126px;height:100px" role="img" aria-label="Fire and smoke damaged room"></div>
    <div class="photo photo--rebuild" style="left:138px;top:124px;width:126px;height:100px" role="img" aria-label="Reconstruction work in progress"></div>
    <span class="tile-label" style="left:10px;top:4px">Water</span>
    <span class="tile-label" style="left:142px;top:4px">Mold</span>
    <span class="tile-label" style="left:10px;top:110px">Fire/Smoke</span>
    <span class="tile-label" style="left:142px;top:110px">Reconstruction</span>
    <p class="contact" style="left:20px;top:268px">www.qualmend.ca<br>Call: 403-771-4286</p>
    <div class="logo" style="left:20px;top:300px"><span class="logo__mark"></span><span class="logo__name">qualmend</span></div>
  </div>
  <div class="panel panel--front">
    <svg class="swirl" viewBox="0 0 270 340" preserveAspectRatio="none" aria-hidden="true">
      <rect width="270" height="340" fill="#1a1b1c"/>
      <path d="M0 170 C90 140 200 150 270 110 V340 H0 Z" fill="#7cc242"/>
      <path d="M0 185 C90 160 200 170 270 130 V340 H0 Z" fill="#2a2c2e"/>
    </svg>
    <div class="tile-label" style="left:10px;top:5px;font-size:8px">Water &nbsp; Mold &nbsp; Fire/Smoke &nbsp; Reconstruction</div>
    <div class="photo photo--house-water" style="left:0;top:20px;width:270px;height:150px;clip-path:path('M0 0 H270 V90 C200 130 90 120 0 150 Z')" role="img" aria-label="Small model house splashing in water"></div>
    <h1 class="headline" style="left:10px;top:196px">When unexpected<br>happens….<br>expect…</h1>
    <ul class="sector-list" style="left:196px;top:198px">
      <li>Residential</li><li>Commercial</li><li>Institutional</li>
    </ul>
    <div class="logo" style="left:100px;top:292px"><span class="logo__mark"></span><span class="logo__name">qualmend</span></div>
    <p class="logo__tag" style="left:108px;top:318px">Complete Restoration &amp; Reconstruction services</p>
  </div>
</section>

<!-- Inside spread -->
<section class="spread spread--inner">
  <div class="panel panel--features">
    <svg class="swirl" viewBox="0 0 270 340" preserveAspectRatio="none" aria-hidden="true">
      <rect width="270" height="340" fill="#1a1b1c"/>
      <path d="M0 0 H60 C30 40 20 80 40 120 L0 130 Z" fill="#1b5fb0"/>
      <path d="M0 250 C80 220 190 230 270 260 V340 H0 Z" fill="#1b5fb0"/>
    </svg>
    <span class="title-dot" style="left:16px;top:18px"></span>
    <h2 class="section-title" style="left:40px;top:12px">Key Features:</h2>
    <ul class="bullets" style="left:24px;top:48px;width:230px">
      <li>BTFQN Certified Firm</li>
      <li>Professionally Managed Company (KDW® certified)</li>
      <li>Excellence, Ethical and Reliable</li>
      <li>Prompt and Competitive Estimates</li>
      <li>Committed to Response within 60 minutes</li>
      <li>Highest Priority for Health &amp; Safety</li>
      <li>Green &amp; Eco-friendly</li>
      <li>Exceptional Customer care</li>
      <li>Cutting Edge, Tested &amp; Approved Restoration Process</li>
      <li>High Quality and Latest Equipments</li>
      <li>24x7 Dedicated &amp; Prompt service</li>
    </ul>
    <div class="photo photo--equipment" style="left:0;top:262px;width:270px;height:78px;clip-path:path('M0 0 C80 -20 190 -10 270 10 V78 H0 Z')" role="img" aria-label="Drying fans and restoration equipment in a room"></div>
  </div>
  <div class="panel panel--capabilities">
    <svg class="swirl" viewBox="0 0 270 340" preserveAspectRatio="none" aria-hidden="true">
      <rect width="270" height="340" fill="#2a2c2e"/>
      <path d="M0 0 H270 V40 C200 20 100 30 0 70 Z" fill="#7cc242"/>
      <path d="M0 340 C60 300 100 260 120 240 L130 340 Z" fill="#7cc242"/>
    </svg>
    <span class="title-dot" style="left:14px;top:18px;background:var(--blue)"></span>
    <h2 class="section-title" style="left:38px;top:12px">Capabilities:</h2>
    <ul class="bullets" style="left:22px;top:48px;width:150px">
      <li>Water Damage Remediation</li>
      <li>Sewer Backup Remediation</li>
      <li>Mold Inspection &amp; Remediation</li>
      <li>Fire/Smoke Damage Remediation</li>
      <li>Structural Drying</li>
      <li>Security Board-up</li>
      <li>Content Pack-out &amp; Cleaning</li>
      <li>Odor Removal &amp; Control</li>
      <li>Carpet Cleaning</li>
      <li>Complete Reconstruction</li>
      <li class="sub">Drywall and Insulation</li>
      <li class="sub">Roofing</li>
      <li class="sub">Flooring</li>
      <li class="sub">Painting</li>
    </ul>
    <div class="photo photo--tech" style="left:165px;top:120px;width:100px;height:210px" role="img" aria-label="Technician in white protective suit and respirator"></div>
  </div>
</section>

<!-- Business cards -->
<article class="card card--front">
  <svg viewBox="0 0 250 145" preserveAspectRatio="none" aria-hidden="true">
    <path d="M0 0 H70 C40 40 40 100 70 145 H0 Z" fill="#1b5fb0"/>
    <path d="M0 0 H52 C28 40 28 100 52 145 H0 Z" fill="#7cc242"/>
    <rect y="128" width="250" height="17" fill="#2a2c2e"/>
  </svg>
  <div class="logo" style="left:62px;top:14px"><span class="logo__mark"></span><span class="logo__name">qualmend</span></div>
  <div class="card__person"><strong>Daniel Mercer</strong>Project Manager<br>Cell: 403-771-4286<br>info@qualmend.ca<br>www.qualmend.ca</div>
  <p class="card__foot" style="left:80px;top:133px">Water Damage • Sewer Backup • Mold • Fire &amp; Smoke</p>
</article>

<article class="card card--front-b">
  <svg viewBox="0 0 250 145" preserveAspectRatio="none" aria-hidden="true">
    <path d="M0 0 H70 C40 40 40 100 70 145 H0 Z" fill="#7cc242"/>
    <path d="M0 0 H52 C28 40 28 100 52 145 H0 Z" fill="#1b5fb0"/>
    <rect y="128" width="250" height="17" fill="#2a2c2e"/>
  </svg>
  <div class="logo" style="left:62px;top:14px"><span class="logo__mark"></span><span class="logo__name">qualmend</span></div>
  <div class="card__person"><strong>Daniel Mercer</strong>Project Manager<br>Office: 403-771-4286<br>120 Bow Trail SW, Calgary</div>
  <p class="card__foot" style="left:80px;top:133px">Water Damage • Sewer Backup • Mold • Fire &amp; Smoke</p>
</article>

<article class="card card--back">
  <svg viewBox="0 0 250 145" preserveAspectRatio="none" aria-hidden="true">
    <rect width="250" height="145" fill="#1a1b1c"/>
    <path d="M0 110 C80 90 170 100 250 80 V145 H0 Z" fill="#1b5fb0"/>
    <path d="M0 122 C80 104 170 112 250 96 V145 H0 Z" fill="#2a2c2e"/>
  </svg>
  <div class="logo" style="left:70px;top:45px"><span class="logo__mark"></span><span class="logo__name">qualmend</span></div>
  <p class="card__foot" style="left:70px;top:72px;color:var(--grey)">Complete Restoration &amp; Reconstruction services</p>
  <p class="card__foot" style="left:62px;top:130px">Water Damage • Sewer Backup • Mold • Fire &amp; Smoke</p>
</article>

</body>
</html>
```